One Page Menu for Food Truck centered on healthy and sustainable eating

This project is a menu for Torvik's - a mobile catering company centered around healthy and sustainable eating.

The menu will be distributed in PDF and print formats. Because of the different mediums, it needs to be one page size.

Our menu will feature three healthy wraps:

The Garden - $7
Filled with Hummus, Fresh Roasted Peppers, Sliced Cucumber, Spinach, Mint Leaves, and Za'tar. (Our vegan option)

The Steak - $8
Filled with Seared Flat Iron Steak, Caramelized Onions, and Blue Cheese.

The Mediterranean - $7
Filled with Marinated Artichoke Hearts, Kalamata Olives, Pepperoncini, and Fresh Squeezed Lemon with a Feta Cheese and Labne Spread.

Torvik's also provides:

Aquas Frescas - $3
A Refreshing Daily Blend of Fruit and Vegetable Purée, Chia Seeds, and Agave Nectar

Jamaica Blue Mountain Reserve Coffee - $2

Water - $1

The design should reflect Torvik's colors of Orange and Green. We would also like a design that incorporates urban gardening, but how is up to you.

Please see website for company - torvik-example.org

Industry/Entity Type

Catering

Requirements
Must have
• Menu items, short descriptions, company logo, Green Colors and Orange Colors

```html
<!DOCTYPE html>
<html lang="en">
<head>
<meta charset="utf-8">
<title>Torvik's Menu</title>
<link rel="stylesheet" href="https://fonts.googleapis.com/css2?family=Exo+2:wght@400;700;800;900&family=Courier+Prime&display=swap">
<style>
  :root {
    --leaf-green: #8cc63f;
    --leaf-green-light: #a3d65c;
    --sun-orange: #f5871f;
    --logo-orange: #f7941d;
    --ink: #111111;
    --arc-ink: #1f3a12;
    --white: #ffffff;
  }
  * { margin: 0; padding: 0; box-sizing: border-box; }
  html, body { width: 927px; height: 1200px; overflow: hidden; }
  body { font-family: "Exo 2", sans-serif; color: var(--ink); }

  .menu-page {
    position: relative;
    width: 927px;
    height: 1200px;
    overflow: hidden;
    background: radial-gradient(circle at 50% 40%, var(--leaf-green-light), var(--leaf-green) 70%);
  }
  .leaf-backdrop {
    position: absolute; inset: 0;
    background: linear-gradient(160deg, rgba(255,255,255,0.12), rgba(255,255,255,0) 60%);
  }
  .sun-disc {
    position: absolute;
    left: 90px; top: 190px;
    width: 770px; height: 770px;
    border-radius: 50%;
    background: var(--sun-orange);
  }
  .arc-lines {
    position: absolute; inset: 0;
    width: 927px; height: 1200px;
  }
  .arc-text {
    font-family: "Courier Prime", monospace;
    font-size: 18px;
    letter-spacing: 3.5px;
    fill: var(--arc-ink);
  }
  .brand-name {
    position: absolute;
    left: 38px; top: 0px;
    font-family: "Exo 2", sans-serif;
    font-weight: 900;
    font-size: 150px;
    line-height: 1;
    color: var(--logo-orange);
  }
  .menu-list {
    position: absolute;
    left: 230px; top: 214px;
    width: 500px;
    text-align: center;
    list-style: none;
  }
  .menu-item { margin-bottom: 20px; }
  .item-name { font-weight: 700; font-size: 19px; line-height: 24px; }
  .item-desc { font-size: 15px; line-height: 22px; }
  .item-line { font-size: 15px; }
  .item-line .item-name { margin-right: 6px; }
  .divider-mark {
    display: block;
    width: 22px; height: 16px;
    margin: -4px auto 14px;
    border-radius: 50%;
    background: var(--leaf-green-light);
  }
  .produce-area {
    position: absolute; left: 0; top: 0;
    width: 927px; height: 1200px;
  }
  .site-url {
    position: absolute;
    left: 240px; top: 1116px;
    font-weight: 800;
    font-size: 21px;
    color: var(--white);
  }
</style>
</head>
<body>
<main class="menu-page">
  <div class="leaf-backdrop" role="img" aria-label="Pattern of pale leaves over the green background"></div>
  <div class="sun-disc"></div>

  <svg class="arc-lines" viewBox="0 0 927 1200" aria-hidden="false">
    <defs>
      <path id="arc-right" d="M 518.7 159.3 A 418 418 0 0 1 893 575"/>
      <path id="arc-left" d="M 75 697 A 418 418 0 0 1 164 296"/>
    </defs>
    <text class="arc-text"><textPath href="#arc-right">FEATURING THREE HEALTHY WRAPS</textPath></text>
    <text class="arc-text"><textPath href="#arc-left">HEALTHY SUSTAINABLE EATING</textPath></text>
  </svg>

  <h1 class="brand-name">Torvik's</h1>

  <ul class="menu-list">
    <li class="menu-item">
      <h2 class="item-name">The Garden</h2>
      <p class="item-desc">Filled with Hummus, Fresh Roasted Peppers, Sliced Cucumber, Spinach, Mint Leaves, and Za’tar.<br>(Our vegan option)&nbsp; $7</p>
    </li>
    <li class="menu-item">
      <h2 class="item-name">The Steak</h2>
      <p class="item-desc">Filled with Seared Flat Iron Steak, Caramelized Onions, and Blue Cheese&nbsp; $8</p>
    </li>
    <li class="menu-item">
      <h2 class="item-name">The Mediterranean</h2>
      <p class="item-desc">Filled with Marinated Artichoke Hearts, Kalamata Olives, Pepperoncini, and Fresh Squeezed Lemon with a Feta Cheese and Labne Spread&nbsp; $7</p>
    </li>
    <li><span class="divider-mark" role="img" aria-label="Small leaf sprig divider"></span></li>
    <li class="menu-item">
      <h2 class="item-name">Aquas Frescas</h2>
      <p class="item-desc">A Refreshing Daily Blend of Fruit and Vegetable Purée, Chia Seeds, and Agave Nectar&nbsp; $3</p>
    </li>
    <li class="menu-item item-line"><span class="item-name">Jamaica Blue Mountain Reserve Coffee</span>$2</li>
    <li class="menu-item item-line"><span class="item-name">Water</span>$1</li>
  </ul>

  <svg class="produce-area" viewBox="0 0 927 1200" role="img" aria-label="Heap of fresh fruit: apples, oranges, mango, avocado, kiwano, limes and a pineapple">
    <defs>
      <linearGradient id="produce-tones" x1="0" y1="0" x2="1" y2="1">
        <stop offset="0" stop-color="#c9d86a"/>
        <stop offset="0.3" stop-color="#e0452c"/>
        <stop offset="0.55" stop-color="#f29a2a"/>
        <stop offset="0.8" stop-color="#3f6a2a"/>
        <stop offset="1" stop-color="#f08a22"/>
      </linearGradient>
    </defs>
    <path fill="url(#produce-tones)" d="M0 1200 L0 840 C80 800 180 720 290 730 C380 690 450 740 560 705 C640 680 700 600 760 540 C810 490 860 440 927 420 L927 1200 Z"/>
  </svg>

  <p class="site-url">www.torvik-example.org</p>
</main>
</body>
</html>
```